Pinecrest Artisan League Membership

UPDATED files - 06/03/2021
Digital brochure needed for construction contractor related nonprofit organization.
Document will be primarily for digital viewing with potential for print version. Should be branded with our branding (logo attached). This is intended to be a multiple page document, plan to print and web (email) use. Standard Letter size document 8.5 x 11 inch
Portrait format preferred
The attached project brief includes a cover, 4 internal pages, and a back cover. This is flexible pending design layout
Target Market(s)
Residential construction business owners
Requirements
Must have
- See attached brief.Orange color palette: RGB: (253,153,0)
Nice to have
- See attached bief
Should not have
- No suit or ties. button up shirt okay, but not white collar worker.

```html
<!DOCTYPE html>
<html lang="en">
<head>
<meta charset="utf-8">
<title>Pinecrest Artisan League Membership Brochure</title>
<link rel="stylesheet" href="https://fonts.googleapis.com/css2?family=Montserrat:wght@500;700;800;900&family=Poppins:wght@300;400;500;600;700&display=swap">
<style>
:root{
  --orange:#f7941d;
  --ink:#2b2b2b;
  --ink-soft:#4a4a4a;
  --paper:#f4f4f4;
  --paper-band:#e7e7e8;
  --stage:#8e8e8e;
  --rule:#3a3a3a;
  --about-bg:#2f2f2f;
}
*{margin:0;padding:0;box-sizing:border-box}
html,body{width:1200px;height:2817px;overflow:hidden}
body{background:var(--stage);position:relative;font-family:"Poppins",sans-serif;color:var(--ink)}

.page{position:absolute;width:calc(var(--u)*100);height:calc(var(--u)*129.4);background:var(--paper);overflow:hidden;box-shadow:0 6px 18px rgba(0,0,0,.25)}
.page.large{--u:6.8px}
.page.medium{--u:5.4px}
.art{position:absolute;inset:0;width:100%;height:100%}

/* brand lockup */
.brand{position:absolute;display:flex;align-items:center;gap:calc(var(--u)*1.2)}
.brand-mark{width:calc(var(--u)*2.6);height:calc(var(--u)*2.6);background:var(--orange);flex:none}
.brand-name{font-family:"Montserrat",sans-serif;font-weight:800;color:var(--ink);text-transform:uppercase;line-height:1;letter-spacing:-.02em}

/* front cover */
.cover-front .brand{left:calc(var(--u)*55);top:calc(var(--u)*7)}
.cover-front .brand-name{font-size:calc(var(--u)*3.6)}
.cover-headline{position:absolute;left:calc(var(--u)*7);top:calc(var(--u)*94);font-family:"Montserrat",sans-serif;font-weight:900;text-transform:uppercase;font-size:calc(var(--u)*4.4);line-height:1.08;letter-spacing:-.01em;color:var(--ink)}
.cover-headline .accent{color:var(--orange)}
.cover-url{position:absolute;left:calc(var(--u)*7);top:calc(var(--u)*117);font-family:"Montserrat",sans-serif;font-weight:700;font-size:calc(var(--u)*2.6);color:var(--ink)}

/* back cover */
.cover-back .brand{left:calc(var(--u)*8);top:calc(var(--u)*104)}
.cover-back .brand-name{font-size:calc(var(--u)*3.4)}
.contact-list{position:absolute;left:calc(var(--u)*47);top:calc(var(--u)*102.5);list-style:none;border-left:calc(var(--u)*.25) solid var(--orange);padding-left:calc(var(--u)*2)}
.contact-list li{display:flex;align-items:center;gap:calc(var(--u)*1.2);font-size:calc(var(--u)*2.3);line-height:1.6;color:var(--ink-soft)}
.contact-list svg{width:1em;height:1em;flex:none}

/* inner pages shared */
.body-copy{font-size:calc(var(--u)*1.7);line-height:1.45;color:var(--ink-soft)}
.section-title{font-family:"Poppins",sans-serif;font-weight:600;text-transform:uppercase;letter-spacing:.02em;line-height:1}
.page-footer .brand{left:calc(var(--u)*8);top:calc(var(--u)*117.5);gap:calc(var(--u)*.8)}
.page-footer .brand-mark{width:calc(var(--u)*1.6);height:calc(var(--u)*1.6)}
.page-footer .brand-name{font-size:calc(var(--u)*2.1)}
.footer-rule{position:absolute;left:calc(var(--u)*33);top:calc(var(--u)*122.4);width:calc(var(--u)*36);height:calc(var(--u)*.3);background:var(--rule)}
.footer-tab{position:absolute;left:calc(var(--u)*68);top:calc(var(--u)*119.8);width:calc(var(--u)*18);height:calc(var(--u)*3);background:var(--orange);clip-path:polygon(12% 0,100% 0,100% 100%,0 100%)}
.footer-tab span{position:absolute;right:calc(var(--u)*1);top:calc(var(--u)*.9);font-size:calc(var(--u)*1.05);color:var(--ink)}
.footer-num{position:absolute;left:calc(var(--u)*86.3);top:calc(var(--u)*119.8);width:calc(var(--u)*3);height:calc(var(--u)*3);background:var(--rule);color:#fff;text-align:center;font-size:calc(var(--u)*1.4);line-height:calc(var(--u)*3)}

/* left inner page */
.pillar-icon{position:absolute;left:calc(var(--u)*8.5);width:calc(var(--u)*9);height:calc(var(--u)*9)}
.pillar-link{position:absolute;left:calc(var(--u)*12.9);width:0;border-left:calc(var(--u)*.3) dotted var(--ink)}
.pillar{position:absolute;left:calc(var(--u)*20);width:calc(var(--u)*62)}
.pillar .section-title{font-size:calc(var(--u)*4.2);color:var(--ink);margin-bottom:calc(var(--u)*1.4)}
.values-list{list-style:none}
.values-list li{display:flex;align-items:center;gap:calc(var(--u)*1.3);margin-bottom:calc(var(--u)*1)}
.values-list svg{width:calc(var(--u)*2);height:calc(var(--u)*2);flex:none}
.values-list span{font-size:calc(var(--u)*1.7);color:var(--ink-soft)}

.about{position:absolute;left:calc(var(--u)*8.5);top:calc(var(--u)*66);width:calc(var(--u)*40);height:calc(var(--u)*47);background:var(--about-bg);padding:calc(var(--u)*2.6) calc(var(--u)*3)}
.about .section-title{font-weight:400;font-size:calc(var(--u)*4.6);color:#fff;margin-bottom:calc(var(--u)*1.6)}
.about .section-title b{color:var(--orange);font-weight:600}
.about .body-copy{color:#e2e2e2;margin-bottom:calc(var(--u)*1.4);font-size:calc(var(--u)*1.5)}
.about-photo{position:absolute;left:calc(var(--u)*48.5);top:calc(var(--u)*66);width:calc(var(--u)*41.5);height:calc(var(--u)*47);background:linear-gradient(135deg,#d8cfc4 0%,#b9ab9b 40%,#7d705f 75%,#4c4238 100%)}

/* right inner page */
.dei-band{position:absolute;left:0;top:0;width:100%;height:calc(var(--u)*42);background:var(--paper-band)}
.dei-title{position:absolute;left:calc(var(--u)*6.5);top:calc(var(--u)*6.5);font-family:"Montserrat",sans-serif;font-weight:800;font-size:calc(var(--u)*4.8);line-height:1.12;text-transform:uppercase;color:var(--ink)}
.dei-title .accent{color:var(--orange)}
.dei-text{position:absolute;left:calc(var(--u)*6.5);top:calc(var(--u)*25);width:calc(var(--u)*33);font-size:calc(var(--u)*1.6)}
.dei-illustration{position:absolute;left:calc(var(--u)*44);top:calc(var(--u)*5);width:calc(var(--u)*50);height:calc(var(--u)*32);border-radius:calc(var(--u)*2);background:linear-gradient(120deg,#dcdcf0 0%,#c7cbe6 45%,#f0c58a 80%,#e9a54a 100%)}

.ta-title{position:absolute;left:calc(var(--u)*6.5);top:calc(var(--u)*46);font-size:calc(var(--u)*4.1);font-weight:300;color:var(--ink)}
.ta-title b{font-weight:600;color:var(--orange)}
.ta-block{position:absolute}
.ta-block strong{color:var(--ink);font-weight:600}
.ta-one{left:calc(var(--u)*6.5);top:calc(var(--u)*53);width:calc(var(--u)*47)}
.ta-two{left:calc(var(--u)*39);top:calc(var(--u)*71);width:calc(var(--u)*55)}
.ta-three{left:calc(var(--u)*6.5);top:calc(var(--u)*91);width:calc(var(--u)*40)}
.ta-illus{position:absolute;border-radius:calc(var(--u)*1.2)}
.ta-illus.one{left:calc(var(--u)*57);top:calc(var(--u)*49);width:calc(var(--u)*17);height:calc(var(--u)*17);background:linear-gradient(160deg,#8fc7f0,#f3b35a 70%,#e27a3a)}
.ta-illus.two{left:calc(var(--u)*10);top:calc(var(--u)*69.5);width:calc(var(--u)*26);height:calc(var(--u)*18);background:linear-gradient(180deg,#dfe7f2,#9fb7d8 55%,#3f5f9a)}
.ta-illus.three{left:calc(var(--u)*51);top:calc(var(--u)*89);width:calc(var(--u)*25);height:calc(var(--u)*15);background:linear-gradient(180deg,#dde6f2,#a8c2e3 55%,#f0b048)}
</style>
</head>
<body>

<!-- Front cover, single view -->
<section class="page large cover-front" style="left:260px;top:80px">
  <svg class="art" viewBox="0 0 100 129.4" preserveAspectRatio="none">
    <defs>
      <linearGradient id="coverPhotoA" x1="0" y1="0" x2="1" y2="1">
        <stop offset="0" stop-color="#c8b9a4"/>
        <stop offset=".35" stop-color="#9aa0a3"/>
        <stop offset=".6" stop-color="#d98a3a"/>
        <stop offset=".85" stop-color="#5a5f66"/>
        <stop offset="1" stop-color="#3b3b3b"/>
      </linearGradient>
    </defs>
    <polygon points="34,20.5 100,20.5 100,23.2 33,23.2" fill="#333"/>
    <g role="img" aria-label="Photo of a contractor in a yellow hard hat and orange safety vest reviewing plans">
      <polygon points="34,24.8 100,24.8 100,80 92,88 52,88 26,56" fill="url(#coverPhotoA)"/>
    </g>
    <polyline points="29.5,26 20.5,56 47.5,91.5 100,91.5" fill="none" stroke="#f7941d" stroke-width="1.6"/>
  </svg>
  <div class="brand"><span class="brand-mark"></span><span class="brand-name">Pinecrest<br>Artisan League</span></div>
  <h1 class="cover-headline"><span class="accent">Helping you<br>reduce risks</span><br>and injuries while<br>improving profitability</h1>
  <p class="cover-url">pinecrestleague.org</p>
</section>

<!-- Outer spread: back cover -->
<section class="page medium cover-back" style="left:60px;top:1060px">
  <div class="brand"><span class="brand-mark"></span><span class="brand-name">Pinecrest<br>Artisan League</span></div>
  <ul class="contact-list">
    <li><svg viewBox="0 0 24 24"><path d="M6.6 10.8a15 15 0 0 0 6.6 6.6l2.2-2.2a1 1 0 0 1 1-.25 11.4 11.4 0 0 0 3.6.57 1 1 0 0 1 1 1V20a1 1 0 0 1-1 1A17 17 0 0 1 3 4a1 1 0 0 1 1-1h3.5a1 1 0 0 1 1 1c0 1.25.2 2.45.57 3.57a1 1 0 0 1-.25 1z" fill="#f7941d"/></svg>(555) 014-2290</li>
    <li><svg viewBox="0 0 24 24"><rect x="2" y="5" width="20" height="14" rx="2" fill="#f7941d"/><path d="M3 6l9 7 9-7" fill="none" stroke="#fff" stroke-width="1.6"/></svg>hello@pinecrestleague.org</li>
    <li><svg viewBox="0 0 24 24"><circle cx="12" cy="12" r="9.5" fill="none" stroke="#f7941d" stroke-width="2"/><ellipse cx="12" cy="12" rx="4" ry="9.5" fill="none" stroke="#f7941d" stroke-width="1.6"/><path d="M2.5 12h19" stroke="#f7941d" stroke-width="1.6"/></svg>pinecrestleague.org</li>
  </ul>
</section>

<!-- Outer spread: front cover -->
<section class="page medium cover-front" style="left:600px;top:1060px">
  <svg class="art" viewBox="0 0 100 129.4" preserveAspectRatio="none">
    <defs>
      <linearGradient id="coverPhotoB" x1="0" y1="0" x2="1" y2="1">
        <stop offset="0" stop-color="#c8b9a4"/>
        <stop offset=".35" stop-color="#9aa0a3"/>
        <stop offset=".6" stop-color="#d98a3a"/>
        <stop offset=".85" stop-color="#5a5f66"/>
        <stop offset="1" stop-color="#3b3b3b"/>
      </linearGradient>
    </defs>
    <polygon points="34,20.5 100,20.5 100,23.2 33,23.2" fill="#333"/>
    <g role="img" aria-label="Photo of a contractor in a yellow hard hat and orange safety vest reviewing plans">
      <polygon points="34,24.8 100,24.8 100,80 92,88 52,88 26,56" fill="url(#coverPhotoB)"/>
    </g>
    <polyline points="29.5,26 20.5,56 47.5,91.5 100,91.5" fill="none" stroke="#f7941d" stroke-width="1.6"/>
  </svg>
  <div class="brand"><span class="brand-mark"></span><span class="brand-name">Pinecrest<br>Artisan League</span></div>
  <h1 class="cover-headline"><span class="accent">Helping you<br>reduce risks</span><br>and injuries while<br>improving profitability</h1>
  <p class="cover-url">pinecrestleague.org</p>
</section>

<!-- Inner spread: left page -->
<section class="page medium inner-left" style="left:60px;top:1880px">
  <svg class="pillar-icon" style="top:calc(var(--u)*7)" viewBox="0 0 40 40"><circle cx="20" cy="20" r="18" fill="none" stroke="#2b2b2b" stroke-width="2.5"/><path d="M20 2a18 18 0 0 1 18 18" fill="none" stroke="#f7941d" stroke-width="2.5"/><circle cx="20" cy="20" r="13" fill="#2b2b2b"/><circle cx="20" cy="20" r="7" fill="none" stroke="#fff" stroke-width="1.5"/><circle cx="20" cy="20" r="3" fill="#f7941d"/></svg>
  <div class="pillar-link" style="top:calc(var(--u)*16.5);height:calc(var(--u)*5)"></div>
  <svg class="pillar-icon" style="top:calc(var(--u)*21.5)" viewBox="0 0 40 40"><circle cx="20" cy="20" r="18" fill="none" stroke="#2b2b2b" stroke-width="2.5"/><path d="M2 20a18 18 0 0 1 18-18" fill="none" stroke="#f7941d" stroke-width="2.5"/><circle cx="20" cy="20" r="13" fill="#2b2b2b"/><path d="M11 20q9-9 18 0q-9 9-18 0z" fill="none" stroke="#fff" stroke-width="1.5"/><circle cx="20" cy="20" r="2.8" fill="#fff"/></svg>
  <div class="pillar-link" style="top:calc(var(--u)*31);height:calc(var(--u)*7)"></div>
  <svg class="pillar-icon" style="top:calc(var(--u)*38)" viewBox="0 0 40 40"><circle cx="20" cy="20" r="18" fill="none" stroke="#2b2b2b" stroke-width="2.5"/><path d="M20 38a18 18 0 0 1-18-18" fill="none" stroke="#f7941d" stroke-width="2.5"/><circle cx="20" cy="20" r="13" fill="#2b2b2b"/><ellipse cx="20" cy="20" rx="8" ry="3.2" fill="none" stroke="#fff" stroke-width="1.2"/><ellipse cx="20" cy="20" rx="8" ry="3.2" fill="none" stroke="#fff" stroke-width="1.2" transform="rotate(60 20 20)"/><ellipse cx="20" cy="20" rx="8" ry="3.2" fill="none" stroke="#fff" stroke-width="1.2" transform="rotate(-60 20 20)"/><circle cx="20" cy="20" r="1.6" fill="#f7941d"/></svg>

  <div class="pillar" style="top:calc(var(--u)*8)">
    <h2 class="section-title">Mission</h2>
    <p class="body-copy">To promote, educate and advance a diverse contractor community by providing pathways of accessibility to help build a stronger foundation for a better future</p>
  </div>
  <div class="pillar" style="top:calc(var(--u)*22.5)">
    <h2 class="section-title">Vision</h2>
    <p class="body-copy">To become the preferred organization for construction contractors striving to be the best in their trade through education, training, and ongoing development</p>
  </div>
  <div class="pillar" style="top:calc(var(--u)*39.5)">
    <h2 class="section-title">Core Values</h2>
    <ul class="values-list">
      <li><svg viewBox="0 0 20 20"><circle cx="10" cy="10" r="9" fill="#f7941d"/><path d="M6 10.5l3 3 5-6" fill="none" stroke="#fff" stroke-width="2"/></svg><span>Empower through learning &amp; development</span></li>
      <li><svg viewBox="0 0 20 20"><circle cx="10" cy="10" r="9" fill="#f7941d"/><path d="M6 10.5l3 3 5-6" fill="none" stroke="#fff" stroke-width="2"/></svg><span>Strengthen &amp; sustain the industry</span></li>
      <li><svg viewBox="0 0 20 20"><circle cx="10" cy="10" r="9" fill="#f7941d"/><path d="M6 10.5l3 3 5-6" fill="none" stroke="#fff" stroke-width="2"/></svg><span>Build partnerships to benefit underserved communities</span></li>
      <li><svg viewBox="0 0 20 20"><circle cx="10" cy="10" r="9" fill="#f7941d"/><path d="M6 10.5l3 3 5-6" fill="none" stroke="#fff" stroke-width="2"/></svg><span>Act with integrity, respect, and honesty</span></li>
      <li><svg viewBox="0 0 20 20"><circle cx="10" cy="10" r="9" fill="#f7941d"/><path d="M6 10.5l3 3 5-6" fill="none" stroke="#fff" stroke-width="2"/></svg><span>Promote diversity, equity, and inclusion throughout the industr</span></li>
    </ul>
  </div>

  <article class="about">
    <h2 class="section-title">About <b>Us</b></h2>
    <p class="body-copy">PAL is organized as a 501c6 membership organization supported by a 501c3 charitable foundation. Our foundation allows us to provide access to training and education resources to an underserved community of contractors, supporting them in developing a sustainable and profitable business.</p>
    <p class="body-copy">We invite you to join a community of contractors who are better prepared to overcome challenges within the industry, empowering them to share ideas, lessons learned, proven practices, and insights with other industry leaders</p>
  </article>
  <div class="about-photo" role="img" aria-label="Photo of contractors studying training materials at a classroom table"></div>

  <footer class="page-footer">
    <div class="brand"><span class="brand-mark"></span><span class="brand-name">Pinecrest<br>Artisan League</span></div>
    <div class="footer-rule"></div>
    <div class="footer-tab"><span>pinecrestleague.org</span></div>
    <div class="footer-num">01</div>
  </footer>
</section>

<!-- Inner spread: right page -->
<section class="page medium inner-right" style="left:600px;top:1880px">
  <div class="dei-band"></div>
  <h2 class="dei-title"><span class="accent">Diversity,</span><br>Equity &amp;<br>Inclusio</h2>
  <p class="body-copy dei-text">PAL promotes and encourages open dialogue and positive working environments for BIPOC and other identity groups, to thrive within a contractor community and facilitate a more inclusive and resilient future</p>
  <div class="dei-illustration" role="img" aria-label="Illustration of a diverse group of construction workers in hard hats in front of a city skyline with cranes"></div>

  <h2 class="section-title ta-title">Technical <b>Assistanc</b></h2>

  <svg class="art" viewBox="0 0 100 129.4" preserveAspectRatio="none" aria-hidden="true">
    <polyline points="54,54 55.5,54 55.5,68 37.5,68 37.5,71" fill="none" stroke="#f7941d" stroke-width=".3" stroke-dasharray=".8 .6"/>
    <polyline points="48,86.5 48,88.5 44,88.5 44,92" fill="none" stroke="#f7941d" stroke-width=".3" stroke-dasharray=".8 .6"/>
  </svg>

  <div class="ta-block ta-one"><p class="body-copy"><strong>One of our primary goals is to provide technical</strong> assistance to the contractor community based on individual level of competency. We understand that the needs of contractors vary greatly based on experience, training, past mentorship.</p></div>
  <div class="ta-illus one" role="img" aria-label="Illustration of a worker beside a house with a light bulb idea"></div>

  <div class="ta-illus two" role="img" aria-label="Illustration of a team of construction workers in front of building cranes"></div>
  <div class="ta-block ta-two"><p class="body-copy"><strong>Technical assistance takes many forms including</strong> business formation assistance, contractor licensing (OR, WA), insurance consulting, access to legal resources as well as assistance with government program funding (PPP Loans, business grants, scholarships), and various networking opportunities.</p></div>

  <div class="ta-block ta-three"><p class="body-copy"><strong>We also provide technical assistance in one-on-one</strong> setting as well as business workshops and ongoing assistance. Additionally, we offer assistance with SBEC initial and renewal applications</p></div>
  <div class="ta-illus three" role="img" aria-label="Illustration of two workers reviewing plans beside a building under construction"></div>

  <footer class="page-footer">
    <div class="brand"><span class="brand-mark"></span><span class="brand-name">Pinecrest<br>Artisan League</span></div>
    <div class="footer-rule"></div>
    <div class="footer-tab"><span>pinecrestleague.org</span></div>
    <div class="footer-num">01</div>
  </footer>
</section>

</body>
</html>
```